Email footer for a cafe

The task is to design an email footer for a new start up cafe business. The logo has been designed, but we would like a professional email footer to sign off on all emails.

The email footer should :
1. look professional and competent
2. be clean and easy to read
3. the email must have the ability to optimise / adjust across the bottom of the email depending on the device being used to read the email
4. the design may stretch across the entire bottom of the email, but this is not mandatory
5. it must incorporate the logo and the details as listed below.
6. For any additional lines / dividers that a designer might choose to incorporate into the email footer, our preference is to match the colour of the logo.

The logo is attached. The logo details are:

The CMYK for the logo is C0 M50 Y100 K0 in font BankGothic Lt BT - Light
The CMKY for the text is C75 M68 Y67 K89 in font AvantGarde Bk BT - Book

The details to be included in the email footer are:

Ted Varro
Founder
0417 283 614
pelvar@brookfieldkitchenqx.com
Unit 6, 14 Malvory Crescent
Tembly KLW 5213

Have fun and thank you in advance for choosing to work on our job.

Reason: Thank you to everyone who has submitted their designs for an email footer. Looking at the designs most have been designed horizontally. Could I please also see some designs where all the elements are under each other in a stacked format. I have attached 2 images which I have grabbed from the internet to be used as an example.

```html
<!DOCTYPE html>
<html lang="en">
<head>
<meta charset="utf-8">
<title>Brookfield Kitchen – Email Footer</title>
<link rel="stylesheet" href="https://fonts.googleapis.com/css2?family=Arimo:wght@400&display=swap">
<style>
  :root {
    --brand-orange: #f7941d;
    --text-dark: #231f20;
    --frame-grey: #8a8a8a;
    --page-bg: #ffffff;
    --social-1: #3b5998;
    --social-2: #35465c;
    --social-3: #a1775a;
    --social-4: #4fb6e8;
    --social-5: #2e8fc6;
  }
  * { margin: 0; padding: 0; box-sizing: border-box; }
  html, body {
    width: 1200px;
    height: 1000px;
    overflow: hidden;
    background: var(--page-bg);
    font-family: "Arimo", Arial, sans-serif;
    color: var(--text-dark);
  }
  .canvas { position: relative; width: 1200px; height: 1000px; }
  .footer-frame {
    position: absolute;
    left: 57px; top: 347px;
    width: 1086px; height: 249px;
    border: 1.5px dashed var(--frame-grey);
  }
  .signature { position: absolute; left: 80px; top: 349px; width: 400px; }
  .person-name {
    font-size: 24px;
    line-height: 28px;
    color: var(--brand-orange);
    font-weight: 400;
  }
  .person-role {
    font-size: 17px;
    line-height: 20px;
    margin-left: 27px;
  }
  .divider {
    width: 187px;
    height: 1px;
    background: var(--brand-orange);
  }
  .divider--top { margin-top: 4px; }
  .brand-lockup {
    width: 187px;
    height: 98px;
    display: flex;
    align-items: center;
    justify-content: center;
    gap: 8px;
  }
  .brand-mark {
    width: 16px; height: 16px;
    border-radius: 50%;
    background: var(--brand-orange);
    flex: none;
  }
  .brand-name {
    font-size: 17px;
    line-height: 20px;
    font-weight: 400;
    color: var(--brand-orange);
    white-space: nowrap;
  }
  .address {
    font-size: 12px;
    line-height: 14px;
    margin-top: 6px;
  }
  .contact-list { list-style: none; margin-top: 4px; }
  .contact-item { font-size: 12px; line-height: 16px; }
  .contact-label { color: var(--brand-orange); margin-right: 6px; }
  .social-row { display: flex; gap: 7px; margin-top: 4px; }
  .social-tile { width: 17px; height: 17px; border-radius: 2px; }
  .social-tile--1 { background: var(--social-1); }
  .social-tile--2 { background: var(--social-2); }
  .social-tile--3 { background: var(--social-3); }
  .social-tile--4 { background: var(--social-4); }
  .social-tile--5 { background: var(--social-5); }
</style>
</head>
<body>
<div class="canvas">
  <div class="footer-frame"></div>
  <div class="signature">
    <p class="person-name">Ted Varro</p>
    <p class="person-role">Founder</p>
    <div class="divider divider--top"></div>
    <div class="brand-lockup">
      <span class="brand-mark"></span>
      <span class="brand-name">Brookfield Kitchen</span>
    </div>
    <div class="divider"></div>
    <p class="address">Unit 6, 14 Malvory Crescent, Tembly KLW 5213</p>
    <ul class="contact-list">
      <li class="contact-item"><span class="contact-label">Phone :</span>0417 283 614</li>
      <li class="contact-item"><span class="contact-label">Email :</span>pelvar@brookfieldkitchenqx.com</li>
      <li class="contact-item"><span class="contact-label">Website :</span>brookfieldkitchen.com</li>
    </ul>
    <div class="social-row" aria-label="Social media links">
      <span class="social-tile social-tile--1"></span>
      <span class="social-tile social-tile--2"></span>
      <span class="social-tile social-tile--3"></span>
      <span class="social-tile social-tile--4"></span>
      <span class="social-tile social-tile--5"></span>
    </div>
  </div>
</div>
</body>
</html>
```